Motivating Modern Poster for Top Selling Reps

We need a poster design for our Sales reps at our Solar company. Our company's mission is to disrupt the energy monopoly and give our customers a choice in how they get their energy. Our sales reps need a street style, modern poster with this quote:
"Practice until you never get it wrong"
Here are a few examples of what has been done previously and our logo. The final design should motivate.

```html
<!DOCTYPE html>
<html lang="en">
<head>
<meta charset="utf-8">
<title>Practice Until You Never Get It Wrong</title>
<link href="https://fonts.googleapis.com/css2?family=Unbounded:wght@900&display=swap" rel="stylesheet">
<style>
  :root {
    --paper: #f2f2e2;
    --sky: #3fbeef;
    --ocean: #1070b8;
    --flame: #e84e1c;
    --sun: #f29104;
    --leaf: #4f9a36;
    --ink: #2a1a10;
  }
  html, body {
    margin: 0;
    padding: 0;
    overflow: hidden;
    background: var(--paper);
  }
  .poster {
    position: relative;
    width: 927px;
    height: 1200px;
    background: var(--paper);
    overflow: hidden;
    font-family: "Unbounded", "Arial Black", sans-serif;
  }
  .art {
    position: absolute;
  }
  .art--bulbs {
    left: 30px;
    top: 0;
    width: 216px;
    height: 380px;
    background: linear-gradient(180deg, rgba(42,26,16,0.10) 0%, rgba(79,154,54,0.28) 70%, rgba(79,154,54,0.12) 100%);
    border-radius: 0 0 40px 40px;
  }
  .art--sun {
    left: 585px;
    top: 16px;
    width: 318px;
    height: 318px;
    border-radius: 50%;
    background: radial-gradient(circle, var(--sun) 0%, rgba(242,145,4,0.75) 55%, rgba(242,145,4,0.15) 100%);
  }
  .headline {
    position: absolute;
    left: 0;
    top: 0;
  }
  .headline text {
    font-family: "Unbounded", "Arial Black", sans-serif;
    font-weight: 900;
  }
  .line--practice { fill: var(--sky); }
  .line--until { fill: var(--ocean); }
  .line--never { fill: var(--flame); }
  .line--wrong, .line--getit { fill: var(--sun); }
  .brand {
    position: absolute;
    left: 712px;
    top: 1112px;
    display: flex;
    align-items: center;
    gap: 8px;
  }
  .brand__dot {
    width: 18px;
    height: 18px;
    border-radius: 50%;
    background: var(--sky);
  }
  .brand__name {
    font-family: "Unbounded", "Arial Black", sans-serif;
    font-weight: 900;
    font-size: 30px;
    color: var(--sky);
    line-height: 1;
  }
</style>
</head>
<body>
  <main class="poster">
    <div class="art art--bulbs" role="img" aria-label="Hanging light bulbs on cords, one glowing green with leaves beneath it"></div>
    <div class="art art--sun" role="img" aria-label="Stylised orange sun with swirling rays"></div>

    <svg class="headline" width="927" height="1200" viewBox="0 0 927 1200" aria-label="Practice until you never get it wrong">
      <text class="line--practice" x="107" y="484" font-size="124" textLength="709" lengthAdjust="spacingAndGlyphs">P<tspan font-size="108">RACTICE</tspan></text>
      <text class="line--until" x="104" y="596" font-size="112" textLength="719" lengthAdjust="spacingAndGlyphs">UNTIL YOU</text>
      <text class="line--never" x="114" y="752" font-size="170" textLength="710" lengthAdjust="spacingAndGlyphs">NEVER</text>
      <text class="line--getit" transform="translate(136 892) rotate(-90)" x="0" y="0" font-size="34" textLength="126" lengthAdjust="spacingAndGlyphs">GET IT</text>
      <text class="line--wrong" x="154" y="886" font-size="154" textLength="668" lengthAdjust="spacingAndGlyphs">WRONG</text>
    </svg>

    <div class="brand">
      <span class="brand__dot"></span>
      <span class="brand__name">Sunvia</span>
    </div>
  </main>
</body>
</html>
```